Brochure Design Project

UCWA
The brochure is intended to be on United Council of Wellness Arts website available for the members to download for the purpose of educating public about benefits of clinical hypnosis and introduce it as possible treatment option. There should be a empty space left on the last page for the member to stamp their office information.
So, the intended audience is general public that might be interested in hypnosis treatment
White on blue is logo of UCWA.
I would like the brochure to have bright complimentary colors with imagery that is used in health care/complimentary medicine - nature, relaxation, etc.
UCWA website is UCWAinfo.net.

```html
<!DOCTYPE html>
<html lang="en">
<head>
<meta charset="utf-8">
<title>Clinical Hypnosis Brochure – Inside Spread</title>
<link rel="stylesheet" href="https://fonts.googleapis.com/css2?family=Open+Sans:wght@400;600;700;800&display=swap">
<style>
  :root {
    --navy: #23215f;
    --paper: #ffffff;
    --ink: #23215f;
    --accent-red: #e3202a;
    --backdrop: #eeeeef;
  }
  * { box-sizing: border-box; margin: 0; padding: 0; }
  html, body {
    width: 1200px; height: 991px; overflow: hidden;
    background: var(--backdrop);
    font-family: "Open Sans", Arial, sans-serif;
    color: var(--ink);
  }
  .spread {
    position: absolute; left: 30px; top: 30px;
    width: 1140px; height: 930px;
    display: flex;
    background: var(--paper);
    box-shadow: 0 10px 30px rgba(0,0,0,.18);
  }
  .panel {
    position: relative; width: 380px; height: 100%;
    font-size: 12.8px; line-height: 1.34;
    overflow: hidden;
  }
  .panel + .panel { border-left: 1px solid rgba(0,0,0,.06); }
  p { margin-bottom: 8px; }
  .band {
    background: var(--navy); color: #fff;
    font-weight: 700; font-size: 18px;
    padding: 8px 26px 5px;
    clip-path: polygon(0 18%, 100% 0, 100% 100%, 0 100%);
    margin: 0 0 9px;
  }
  .copy { padding: 0 28px; }

  /* left panel */
  .photo { display: block; width: 380px; height: 300px; }
  .panel--left .band { margin-top: -4px; }
  .panel--left .band--second { margin-top: 10px; }

  /* middle panel */
  .panel--middle { background: var(--navy); color: #fff; }
  .panel--middle .top-wedge {
    position: absolute; left: 0; top: 0; width: 100%; height: 44px;
    background: var(--paper);
    clip-path: polygon(0 0, 100% 0, 0 100%);
  }
  .panel--middle .divider {
    position: absolute; left: 0; top: 496px; width: 100%; height: 56px;
    background: var(--paper);
    clip-path: polygon(0 100%, 100% 0, 100% 22%, 0 100%);
  }
  .mid-heading {
    position: relative; font-weight: 700; font-size: 18px;
    padding: 0 28px; margin-bottom: 7px;
  }
  .why { position: absolute; top: 52px; left: 0; right: 0; }
  .when { position: absolute; top: 560px; left: 0; right: 0; }
  .panel--middle .copy { text-align: justify; }
  .list { list-style: none; padding: 0 28px; font-size: 12.2px; line-height: 1.3; }
  .list li { position: relative; padding-left: 22px; }
  .list li::before {
    content: ""; position: absolute; left: 3px; top: 5px;
    width: 6px; height: 6px;
    border-right: 2px solid currentColor; border-top: 2px solid currentColor;
    transform: rotate(45deg);
  }

  /* right panel */
  .panel--right .list { padding-top: 22px; margin-bottom: 12px; color: var(--ink); }
  .panel--right .copy { text-align: justify; }
  .highlight { color: var(--accent-red); }
  .advice {
    margin: 10px 28px 0;
    border: 2px solid var(--navy);
    padding: 10px 12px;
    color: var(--accent-red); font-weight: 700; font-size: 13.6px;
    text-align: center; line-height: 1.3;
  }
</style>
</head>
<body>
<main class="spread">

  <section class="panel panel--left">
    <svg class="photo" viewBox="0 0 380 300" role="img" aria-label="Photo of a woman lying relaxed with closed eyes during a hypnosis session">
      <defs>
        <linearGradient id="photoTone" x1="0" y1="0" x2="1" y2="1">
          <stop offset="0" stop-color="#d7a98a"/>
          <stop offset=".45" stop-color="#f3efee"/>
          <stop offset="1" stop-color="#ecdcd2"/>
        </linearGradient>
      </defs>
      <rect width="380" height="300" fill="#fff"/>
      <path d="M0 55 L380 0 L380 155 C330 265 200 300 60 272 L0 258 Z" fill="url(#photoTone)"/>
      <path d="M0 258 L60 272 C200 300 330 265 380 155 L380 175 C330 283 200 315 55 290 L0 278 Z" fill="var(--navy)"/>
    </svg>
    <h2 class="band">What it is</h2>
    <div class="copy">
      <p>Hypnosis is considered to be a state of focused attention and inner absorption there is decreased awareness of surroundings and increased ability to respond to acceptable suggestions.</p>
      <p>A collaborative process that helps a person's mind and body function more comfortably and effectively.</p>
      <p>It is not uncommon for all of us to experience a situation when we are so preoccupied with a thought or experience that we neglect surroundings. Examples – watching a favorite show, computer games or driving under "highway" hypnosis.</p>
      <p>It requires special training to use hypnosis appropriately in medicine, dentistry and psychotherapy and should be done by licensed professionals in respected fields.</p>
    </div>
    <h2 class="band band--second">What it is not</h2>
    <div class="copy">
      <p>It is not a mind control, just a suggestion.</p>
      <p>It cannot be imposed on an unwilling or uninterested person</p>
      <p>It is not a miracle or cure, but a way to solve some problems.</p>
    </div>
  </section>

  <section class="panel panel--middle">
    <div class="top-wedge"></div>
    <div class="why">
      <h2 class="mid-heading">Why use hypnosis</h2>
      <div class="copy">
        <p>Hypnosis is unique in its ability to help you unlock imagination, bypass the "can never happen" censor of the conscious mind, and simply help one see experiences and memories in a different light.</p>
        <p>It can help find solutions and resolutions to a difficult mental or physical problem, and find inner sources of strength and resilience.</p>
        <p>It can help a person better understand one's own as well as others' motivations and behavior.</p>
        <p>It allows a person to choose and develop abilities and capacities that can help achieve a desired goal.</p>
        <p>During the process of hypnosis a person is frequently taught how use individualized cues and techniques to achieve desired result (decrease anxiety, reduce pain, improve sport performance, etc.) With practice, a person can achieve a level of control that seemed impossible before.</p>
      </div>
    </div>
    <div class="divider"></div>
    <div class="when">
      <h2 class="mid-heading">When</h2>
      <div class="copy">
        <p>Hypnosis has been found to be very effective for treating many mental and physical conditions, as well improving physical and mental performance, and changing undesirable habits.</p>
        <p>Its applications can include:</p>
      </div>
      <ul class="list">
        <li>anxiety disorders;</li>
        <li>coping with emotional and physical trauma;</li>
        <li>insomnia;</li>
        <li>acute and chronic pain relief;</li>
        <li>preparation for surgical procedures;</li>
        <li>childbirth;</li>
        <li>decreasing side effects of chemotherapy and radiation;</li>
        <li>gastrointestinal disorders;</li>
        <li>asthma;</li>
      </ul>
    </div>
  </section>

  <section class="panel panel--right">
    <ul class="list">
      <li>sports performance and tests preparation;</li>
      <li>fear of flying and</li>
      <li>smoking cessation and weight control</li>
    </ul>
    <h2 class="band">HOW</h2>
    <div class="copy">
      <p>A person conducting hypnosis will walk you through the process, help define goals and expectations, and explain how you can achieve the results you want.
      <span class="highlight">Hypnosis starts with an induction process:</span>
      you simply concentrate on an object, idea or symbol. Induction is followed by relevant communication and crafting of the suggestion. The last step is reorientation and discussion of the experience, and instruction on home practice. All hypnosis is ultimately a form of self hypnosis.</p>
    </div>
    <h2 class="band">Is Hypnosis right for me?</h2>
    <div class="copy">
      <p>Hypnosis is a wonderful and effective tool. If you are not familiar with hypnosis, you might worry about loss of control and embarrassment. People are also worried that their problems cannot be helped.</p>
      <p>Hypnosis might offer a novel way to approach or resolve the problem, or just see it in a different light.</p>
      <p>Even if hypnosis does not immediately solve the problem, you can still learn how to be a little more comfortable and experience a deeper level of physical and mental relaxation.</p>
      <p class="highlight">Practice will help.</p>
      <p>Well-trained medical or mental health professionals will help you discover and use resources and strengths that you did not know you had.</p>
    </div>
    <p class="advice">Your therapist, doctor or dentist might be the best person to discuss hypnosis and how it can be helpful to you.</p>
  </section>

</main>
</body>
</html>
```